Redesign of Bright Harbor Entertainment Card

I already have my logo and font design for my company name. I am looking to come up with a Unique way of having it on my business card. Just looking for a really hip, and professional business card while still using my logo design.

I have also enclosed the front and back of the card so you can see what I have now. Looking for something different.

Thank you!

Target Market(s)

Young to middle aged brides and grooms

Industry/Entity Type

Business

Requirements
Should not have
• Cheese

```html
<!DOCTYPE html>
<html lang="en">
<head>
<meta charset="utf-8">
<title>Bright Harbor Entertainment</title>
<link rel="stylesheet" href="https://fonts.googleapis.com/css2?family=Arimo:wght@700&display=swap">
<style>
  :root {
    --bg: #000000;
    --band: #40c4ff;
    --disc: #2a63f5;
    --ink: #ffffff;
  }
  html, body {
    margin: 0;
    padding: 0;
    background: var(--bg);
    overflow: hidden;
  }
  .card {
    position: relative;
    width: 1200px;
    height: 686px;
    background: var(--bg);
    font-family: "Arimo", Arial, sans-serif;
    font-weight: 700;
    color: var(--ink);
  }
  .brand-disc {
    position: absolute;
    left: 405px;
    top: 33px;
    width: 392px;
    height: 392px;
  }
  .brand {
    position: absolute;
    left: 405px;
    top: 33px;
    width: 392px;
    height: 392px;
    margin: 0;
    display: flex;
    flex-direction: column;
    align-items: center;
    justify-content: center;
    text-align: center;
    font-size: 44px;
    line-height: 54px;
    font-weight: 700;
    color: var(--ink);
  }
  .service {
    position: absolute;
    display: flex;
    align-items: center;
    justify-content: center;
    background: var(--band);
    color: var(--ink);
    font-size: 46px;
    line-height: 1;
    white-space: nowrap;
  }
  .service--djs      { left: 42px;  top: 474px; width: 366px; height: 80px; }
  .service--booths   { left: 417px; top: 474px; width: 365px; height: 80px; }
  .service--montages { left: 792px; top: 474px; width: 365px; height: 80px; }
  .service--lighting { left: 42px;  top: 562px; width: 1115px; height: 80px; }
</style>
</head>
<body>
  <main class="card">
    <svg class="brand-disc" viewBox="0 0 392 392" aria-hidden="true">
      <circle cx="196" cy="196" r="190" fill="var(--disc)" stroke="var(--band)" stroke-width="9"/>
    </svg>
    <h1 class="brand"><span>Bright Harbor</span><span>Entertainment</span></h1>
    <div class="service service--djs">DJs / Emcees</div>
    <div class="service service--booths">Photo Booths</div>
    <div class="service service--montages">Photo Montages</div>
    <div class="service service--lighting">Lighting&nbsp; / Wireless LED Uplighting</div>
  </main>
</body>
</html>
```